Brennock Metal recycling, a business card/logo for our industrial family metal recycling company

A new business card design/logo for our long established family metal recycling company.
I have a logo for our property company which was designed a few months ago on pixel forum which I would like to be very close to this design but have a more industrial feel to it and in a darker blue colour, please see attachments.

Target Market(s)

industries that produce metal waste for recycling, construction sites, engineering companies, manufactures, builders, plumbers, electricians, general house holders.

Industry/Entity Type

Recycling

Contact Information for Business Card

owner/director...Gordon brennock
e-mail....info@brennockscrapworks.example.co.uk
web address.....brennockscrapworks.example.co.uk

Font styles to use
Serif
Sans Serif

Colors
0255a3
ffffff

Requirements
Must have
• -dark blue business card on front.
-white on the back, see contact details, e-mail address for metal company.
-to have an industrial feel to it.
-brennock logo as business card attached but (brennock metal recycling)
please remove the little roof/arrow above brennock as this was relevant to property company.
Nice to have
• please see our website brennockscrapworks.example.co.uk with all details
being correct however I would like to refresh the logo to more like the brennock property investment business card logo attached.
Should not have
• should not contain details from property investments card as this design is for the metal recycling company.

```html
<!DOCTYPE html>
<html lang="en">
<head>
<meta charset="utf-8">
<title>Brennock Metal Recycling – Business Card</title>
<link rel="stylesheet" href="https://fonts.googleapis.com/css2?family=Archivo:wght@700&family=Barlow+Condensed:wght@600&family=Questrial&display=swap">
<style>
  :root {
    --card-blue: #1f4f9a;
    --card-grey: #454545;
    --card-white: #f3f3f1;
    --text-dark: #333333;
    --page-bg: #d9dadc;
  }
  * { margin: 0; padding: 0; box-sizing: border-box; }
  html, body {
    width: 1200px;
    height: 936px;
    overflow: hidden;
    background: var(--page-bg);
  }
  .card {
    position: absolute;
    left: 100px;
    top: 162px;
    width: 1000px;
    height: 612px;
    background: var(--card-white);
    overflow: hidden;
    box-shadow: 0 6px 24px rgba(0,0,0,0.18);
  }
  .brand {
    position: absolute;
    left: 47px;
    top: 74px;
    width: 510px;
    color: var(--card-blue);
    font-family: "Archivo", sans-serif;
    font-weight: 700;
  }
  .brand-name {
    font-size: 74px;
    line-height: 1;
    letter-spacing: 14px;
  }
  .brand-tagline {
    margin-top: 6px;
    margin-left: 48px;
    font-size: 21px;
    letter-spacing: 9px;
    line-height: 1;
  }
  .holder {
    position: absolute;
    left: 47px;
    top: 270px;
  }
  .holder-name {
    font-family: "Barlow Condensed", sans-serif;
    font-weight: 600;
    font-size: 44px;
    line-height: 1.1;
    color: var(--card-blue);
  }
  .holder-role {
    font-family: "Questrial", sans-serif;
    font-size: 25px;
    color: var(--text-dark);
    margin-top: 2px;
  }
  .contacts {
    position: absolute;
    left: 44px;
    top: 432px;
    list-style: none;
    font-family: "Questrial", sans-serif;
    font-size: 26px;
    color: var(--text-dark);
  }
  .contacts li {
    display: flex;
    align-items: center;
    height: 38px;
  }
  .contacts svg {
    width: 26px;
    height: 26px;
    margin-right: 12px;
    flex: none;
  }
  .corner-stripes {
    position: absolute;
    left: 0;
    top: 0;
    width: 1000px;
    height: 612px;
  }
</style>
</head>
<body>
  <div class="card">
    <svg class="corner-stripes" viewBox="0 0 1000 612" aria-hidden="true">
      <polygon points="582,612 1000,150 1000,612" fill="var(--card-blue)"/>
      <polygon points="730,612 1000,307 1000,612" fill="var(--card-grey)"/>
      <polygon points="876,612 1000,464 1000,612" fill="var(--card-blue)"/>
    </svg>

    <div class="brand">
      <div class="brand-name">BRENNOCK</div>
      <div class="brand-tagline">METAL RECYCLING</div>
    </div>

    <div class="holder">
      <div class="holder-name">Gordon brennock</div>
      <div class="holder-role">Owner/Director</div>
    </div>

    <ul class="contacts">
      <li>
        <svg viewBox="0 0 24 24" fill="none" stroke="var(--card-blue)" stroke-width="1.6" aria-hidden="true">
          <circle cx="12" cy="12" r="10"/>
          <path d="M8.5 7.5c-.8.6-1 1.6-.5 2.8 1 2.3 2.6 4 4.9 5.1 1.1.5 2.1.3 2.8-.5l-1.8-1.6-1.2.7c-1.2-.6-2.2-1.6-2.8-2.8l.7-1.2z"/>
        </svg>
        020-5550-1847
      </li>
      <li>
        <svg viewBox="0 0 24 24" fill="none" stroke="var(--card-blue)" stroke-width="1.6" aria-hidden="true">
          <rect x="2" y="5" width="20" height="14"/>
          <path d="M2 5l10 8 10-8M2 19l7-6M22 19l-7-6"/>
        </svg>
        info@brennockscrapworks.example.co.uk
      </li>
      <li>
        <svg viewBox="0 0 24 24" fill="none" stroke="var(--card-blue)" stroke-width="1.6" aria-hidden="true">
          <circle cx="12" cy="12" r="10"/>
          <ellipse cx="12" cy="12" rx="4.5" ry="10"/>
          <path d="M2 12h20M4 7h16M4 17h16"/>
        </svg>
        www.brennockscrapworks.example.co.uk
      </li>
    </ul>
  </div>
</body>
</html>
```